Polystyrene Recycling Material Flow

We need a diagram styled as an infographic that shows how polystyrene foam is recycled starting with a manufactured product, moving through the distribution process, waste material collection and reincorporation back into manufacturing. This is accomplished in different ways once the material is collected which needs to be clearly evident. The most important thing is for it to be simple enough to understand while still having a stylish look. The design can be with or without vector images or photography to depict the different stages. We are providing a very rudimentary 'sketch' of the information points and movement flow. Please see www.foamtradeguild.org (resources) to view our literature branding. The RGB & CMYK are attached.

Target Market(s)

Government Agencies, Brand Owners, Retailers, Recycling Industry

Industry/Entity Type

Packaging, Recycling, Manufacturing

Font styles to use
Sans Serif

Requirements
Must have
• Easy to Understand
Nice to have
• Images - either photography or vector illustrations - are optional. We have provided examples of both to show what could be used but are not required. Substituting your own interpretation of imagery is encouraged.
Should not have
• Outdated look.

```html
<!DOCTYPE html>
<html lang="en">
<head>
<meta charset="utf-8">
<title>Polystyrene Recycling Material Flow</title>
<link href="https://fonts.googleapis.com/css2?family=Plus+Jakarta+Sans:wght@400;500;600;800&display=swap" rel="stylesheet">
<style>
  :root{
    --orange:#F05A22;
    --teal:#165C7D;
    --ink:#0B0B0B;
    --line:#1A1A1A;
    --paper:#FFFFFF;
    --label:#222222;
  }
  *{box-sizing:border-box;margin:0;padding:0}
  html,body{width:1034px;height:1200px;overflow:hidden;background:var(--paper)}
  body{position:relative;font-family:"Plus Jakarta Sans",Arial,sans-serif;color:var(--label)}
  .connectors{position:absolute;left:0;top:0;width:1034px;height:1200px}
  .abs{position:absolute}

  .source{border-radius:9px;overflow:hidden;display:flex;align-items:flex-end;padding:0 0 10px 24px;color:#fff;font-size:12px;font-weight:500}
  .source span{position:relative;text-shadow:0 1px 3px rgba(0,0,0,.5)}

  .pill{height:30px;background:var(--ink);border-radius:15px;color:#fff;font-size:11px;font-weight:500;display:flex;align-items:center;padding-left:52px}
  .pill .thumb{position:absolute;left:0;top:50%;width:45px;height:45px;margin-top:-22.5px;border-radius:50%}
  .pill.sm{height:32px;border-radius:16px}

  .card{background:var(--paper);border-radius:9px;box-shadow:0 2px 10px rgba(0,0,0,.08);overflow:hidden}
  .card .photo{height:110px;border-radius:9px}
  .card .label{font-size:10px;padding:14px 0 0 16px;color:var(--label)}

  .feature{background:var(--teal);border-radius:9px;display:flex;height:110px;overflow:hidden;box-shadow:0 2px 10px rgba(0,0,0,.08)}
  .feature .photo{width:185px;height:100%;border-radius:9px;flex:none}
  .feature .text{color:#fff;font-size:14px;line-height:1.5;font-weight:500;display:flex;align-items:center}

  .collection{left:389px;top:284px;width:255px;height:70px;background:var(--orange);border-radius:35px;display:flex;align-items:center;color:#fff;font-weight:800;font-size:23px;letter-spacing:.5px}
  .collection .icon{width:50px;height:50px;border-radius:50%;background:#fff;margin:0 20px 0 14px;display:flex;align-items:center;justify-content:center}
</style>
</head>
<body>

<svg class="connectors" viewBox="0 0 1034 1200" aria-hidden="true">
  <defs>
    <marker id="head" viewBox="0 0 10 10" refX="8" refY="5" markerWidth="5" markerHeight="5" orient="auto">
      <path d="M0 0L10 5L0 10z" fill="#1A1A1A"/>
    </marker>
    <marker id="headTeal" viewBox="0 0 10 10" refX="8" refY="5" markerWidth="5" markerHeight="5" orient="auto">
      <path d="M0 0L10 5L0 10z" fill="#165C7D"/>
    </marker>
  </defs>
  <g fill="none" stroke="#1A1A1A" stroke-width="0.9">
    <path d="M190 186V240H464V276" marker-end="url(#head)"/>
    <path d="M529 186V276" marker-end="url(#head)"/>
    <path d="M700 186V240H578V276" marker-end="url(#head)"/>
    <path d="M529 360V392"/>
    <path d="M176 392H780"/>
    <path d="M176 392V432" marker-end="url(#head)"/>
    <path d="M780 392V432" marker-end="url(#head)"/>
    <path d="M176 590H383"/>
    <path d="M176 590V622" marker-end="url(#head)"/>
    <path d="M383 590V622" marker-end="url(#head)"/>
    <path d="M649 582V616" marker-end="url(#head)"/>
    <path d="M176 783V816" marker-end="url(#head)"/>
    <path d="M383 783V816" marker-end="url(#head)"/>
    <path d="M649 783V818" marker-end="url(#head)"/>
    <path d="M176 977V1013" marker-end="url(#head)"/>
    <path d="M269 99H279" marker-end="url(#head)"/>
    <path d="M269 152H279" marker-end="url(#head)"/>
    <path d="M776 98H786" marker-end="url(#head)"/>
    <path d="M776 151H786" marker-end="url(#head)"/>
    <path d="M271 485H288" marker-end="url(#head)"/>
    <path d="M271 546H288" marker-end="url(#head)"/>
    <path d="M736 666H756" marker-end="url(#head)"/>
    <path d="M736 724H756" marker-end="url(#head)"/>
  </g>
  <g fill="none" stroke="#165C7D" stroke-width="1">
    <path d="M76 1078H45V317H363" marker-end="url(#headTeal)"/>
    <path d="M953 887H985V317H668" marker-end="url(#headTeal)"/>
  </g>
</svg>

<!-- Sources -->
<div class="abs source" style="left:125px;top:78px;width:143px;height:100px;background:linear-gradient(180deg,#5b7fa3 0%,#7b6f62 45%,#3d3a36 100%)" role="img" aria-label="Photo of a municipal waste heap under canopies"><span>Municipal Waste</span></div>
<div class="abs pill" style="left:279px;top:84px;width:168px">
  <div class="thumb" style="background:linear-gradient(90deg,#d13b2f,#f0b12a,#3a8a3d,#2c5aa8)" role="img" aria-label="Photo of curbside recycling bins"></div>Curbside Collection</div>
<div class="abs pill" style="left:279px;top:140px;width:168px">
  <div class="thumb" style="background:radial-gradient(circle at 40% 50%,#e0a02a,#6e6a4a 60%,#3b3b35)" role="img" aria-label="Photo of a drop-off recycling bin"></div>Drop-Off Centers</div>

<div class="abs source" style="left:468px;top:78px;width:143px;height:100px;padding-left:8px;background:linear-gradient(180deg,#c9a33c 0%,#6d9cb8 40%,#2c6f95 100%)" role="img" aria-label="Photo of a sorting conveyor with manufacturing scrap"><span>Manufacturing Waste</span></div>

<div class="abs source" style="left:632px;top:77px;width:143px;height:100px;padding-left:17px;background:linear-gradient(180deg,#b9bcc0 0%,#b58a5a 40%,#23477a 100%)" role="img" aria-label="Photo of an overflowing commercial dumpster"><span>Commercial Waste</span></div>
<div class="abs pill" style="left:789px;top:81px;width:169px">
  <div class="thumb" style="background:linear-gradient(135deg,#3a6ea8,#b8582e 60%,#2c3e66)" role="img" aria-label="Photo of a delivery truck at a loading dock"></div>Back Hauling</div>
<div class="abs pill" style="left:789px;top:137px;width:169px">
  <div class="thumb" style="background:radial-gradient(circle at 50% 55%,#3aa35a,#4a5a52 60%,#2c302e)" role="img" aria-label="Photo of a local recycling delivery bin"></div>Localized Delivery</div>

<!-- Collection -->
<div class="abs collection">
  <div class="icon">
    <svg width="24" height="26" viewBox="0 0 24 26" aria-hidden="true" fill="none" stroke="#F05A22" stroke-width="2.2" stroke-linecap="round">
      <path d="M2 5H22M9 5V2H15V5"/><path d="M4 5L5.5 24H18.5L20 5"/><path d="M9.5 9V20M14.5 9V20"/>
    </svg>
  </div>COLLECTION
</div>

<!-- Compaction branch -->
<div class="abs card" style="left:85px;top:440px;width:185px;height:141px">
  <div class="photo" style="background:linear-gradient(135deg,#8a7256 0%,#a78c63 40%,#5b6e4a 70%,#3f4a5a 100%)" role="img" aria-label="Photo of a worker with a tablet beside a compaction baler"></div>
  <div class="label" style="padding-top:10px">Compaction</div>
</div>
<div class="abs pill sm" style="left:297px;top:470px;width:150px">
  <div class="thumb" style="background:linear-gradient(135deg,#9fb3c8,#3f5266 55%,#c9d6e2)" role="img" aria-label="Photo of extruded polystyrene ingots"></div>Extruded Ingot</div>
<div class="abs pill sm" style="left:297px;top:528px;width:182px">
  <div class="thumb" style="background:linear-gradient(135deg,#c08a4a,#6d6a63 55%,#3c3a36)" role="img" aria-label="Photo of a hydraulic compression machine"></div>Hydrolic Compression</div>

<div class="abs card" style="left:82px;top:632px;width:185px;height:145px">
  <div class="photo" style="background:radial-gradient(circle at 50% 55%,#ffffff 0%,#e7e7e9 45%,#c9c6c4 100%)" role="img" aria-label="Photo of hands holding white polystyrene resin beads"></div>
  <div class="label">Recycled Content EPS Resin</div>
</div>
<div class="abs card" style="left:299px;top:632px;width:185px;height:145px">
  <div class="photo" style="background:radial-gradient(circle,#f2f2f2 0%,#cfcfcf 60%,#a9a9a9 100%)" role="img" aria-label="Photo of grey rigid polystyrene pellets"></div>
  <div class="label">Extruded Rigid PS Pellet</div>
</div>

<div class="abs card" style="left:82px;top:826px;width:185px;height:145px">
  <div class="photo" style="background:linear-gradient(135deg,#d9dfe6 0%,#b9cad8 45%,#dcc49c 100%)" role="img" aria-label="Photo of clear re-pelletized plastic granules"></div>
  <div class="label">Re-Pelletized With Blowing Agent</div>
</div>
<div class="abs card" style="left:299px;top:826px;width:185px;height:145px">
  <div class="photo" style="background:linear-gradient(135deg,#2b3e63 0%,#8c7b66 40%,#4a4d55 70%,#2a5bb0 100%)" role="img" aria-label="Photo of workers sorting material on a conveyor"></div>
  <div class="label">End Market Applications</div>
</div>

<div class="abs feature" style="left:82px;top:1023px;width:403px">
  <div class="photo" style="background:linear-gradient(135deg,#d9dfe6 0%,#b9cad8 45%,#dcc49c 100%)" role="img" aria-label="Photo of clear polystyrene granules"></div>
  <div class="text" style="padding-left:36px">Expanded Polystyrene<br>Packaging &amp; Building<br>Products ≤50%</div>
</div>

<!-- Regrind branch -->
<div class="abs feature" style="left:552px;top:459px;width:402px">
  <div class="photo" style="background:radial-gradient(circle at 55% 55%,#d9c26a 0%,#6e8a7a 40%,#3a4048 100%)" role="img" aria-label="Photo of hands holding a bag of colourful plastic regrind"></div>
  <div class="text" style="padding-left:44px">Regrind -<br>Molder Facilities</div>
</div>

<div class="abs card" style="left:550px;top:630px;width:185px;height:145px">
  <div class="photo" style="background:linear-gradient(180deg,#5f7e8a 0%,#c98a52 45%,#b5652e 100%)" role="img" aria-label="Photo of a pile of shredded material"></div>
  <div class="label">Shredding</div>
</div>
<div class="abs pill" style="left:766px;top:652px;width:168px">
  <div class="thumb" style="background:linear-gradient(135deg,#cfd3d2,#8d9694 60%,#5e6664)" role="img" aria-label="Photo of a homogenization machine"></div>Homogenization</div>
<div class="abs pill" style="left:766px;top:708px;width:190px">
  <div class="thumb" style="background:linear-gradient(135deg,#e6eef2,#9fb0bb 60%,#6d7c86)" role="img" aria-label="Photo of an industrial mixing unit"></div>Mixing for Consistency</div>

<div class="abs feature" style="left:550px;top:826px;width:402px">
  <div class="photo" style="background:radial-gradient(circle at 50% 60%,#f5f1ea 0%,#c9a77c 45%,#8e8a86 100%)" role="img" aria-label="Photo of a cardboard box filled with foam packing peanuts"></div>
  <div class="text" style="padding-left:36px">Recycled Content<br>Packaging ≤15%</div>
</div>

</body>
</html>
```